Professional Modern Website Design

We are a premium IT services provider to the financial industry based in London. Our company is called Veltra our current holding page is www.veltra-example.co.uk. We require a new website to match our new corporate identity. This project is for the design phase only. Development will be handled in-house. I have attached examples of wire frames we have developed (although open to suggestions for improvement) Our brand document that should demonstrate current brand, inc how we communicate to potential clients and finally mostly completed web-content.
We are looking for designers that can create something that sets us apart from our competitors.
Target Market(s)
IT Decision makers in Finance companies such as; hedge funds, private investment banks etc
Industry/Entity Type
Financial
Number of Pages Required
5+ page
Requirements
Must have
- hexagon elements in the design, unique design.
Nice to have
- Blog and social media feeds
Should not have
- Should not resemble a downloaded template

```html
<!DOCTYPE html>
<html lang="en">
<head>
<meta charset="utf-8">
<title>Veltra — IT Integration for Finance</title>
<link rel="stylesheet" href="https://fonts.googleapis.com/css2?family=Dosis:wght@300;400;500&family=Open+Sans:wght@400;600;700&display=swap">
<style>
  :root {
    --orange: #f5821f;
    --orange-soft: rgba(238, 128, 34, 0.88);
    --ink: #3a3a3a;
    --nav: #444444;
    --white: #ffffff;
    --dark-1: #1e1e1e;
    --dark-2: #2c2c2c;
    --footer-bar: #3d3d3d;
    --btn-dark: #3f3f3f;
  }
  * { box-sizing: border-box; margin: 0; padding: 0; }
  html, body { width: 825px; height: 1200px; overflow: hidden; background: var(--white); }
  body { position: relative; font-family: "Open Sans", Arial, sans-serif; color: var(--ink); }

  /* Header */
  .site-header { position: absolute; left: 0; top: 0; width: 825px; height: 82px; background: var(--white); }
  .brand { position: absolute; left: 82px; top: 24px; display: flex; align-items: center; gap: 6px; }
  .brand-mark { width: 14px; height: 14px; background: var(--orange); }
  .brand-name { font-family: "Dosis", sans-serif; font-weight: 500; font-size: 20px; color: var(--orange); letter-spacing: 1px; }
  .follow { position: absolute; right: 84px; top: 13px; font-family: "Dosis", sans-serif; font-size: 8px; letter-spacing: .5px; color: #8a8a8a; }
  .main-nav { position: absolute; right: 84px; top: 39px; display: flex; gap: 19px; }
  .main-nav a { font-family: "Dosis", sans-serif; font-size: 11.5px; letter-spacing: .4px; color: var(--nav); text-decoration: none; }
  .main-nav a.is-active { color: var(--orange); }

  /* Hero */
  .hero { position: absolute; left: 0; top: 82px; width: 825px; height: 343px; }
  .hero-photo { position: absolute; inset: 0; background: linear-gradient(180deg, #4a4a4a 0%, #3a3a3a 45%, #2a2a2a 70%, #1c1c1c 100%); }
  .hero-panel { position: absolute; left: 223px; top: 118px; width: 379px; height: 120px; background: var(--orange-soft); text-align: center; padding-top: 27px; }
  .hero-title { font-family: "Dosis", sans-serif; font-weight: 300; font-size: 15px; line-height: 18px; color: var(--white); letter-spacing: .2px; }
  .hero-text { margin: 6px auto 0; width: 345px; font-size: 10.2px; line-height: 12.5px; color: var(--white); }
  .hero-cta { position: absolute; left: 361px; top: 245px; width: 102px; height: 26px; background: var(--orange); color: var(--white); font-family: "Dosis", sans-serif; font-size: 12.5px; letter-spacing: .5px; line-height: 26px; text-align: center; }

  /* Who we are */
  .about { position: absolute; left: 0; top: 425px; width: 825px; height: 522px; }
  .about-photo { position: absolute; inset: 0; background: radial-gradient(ellipse at 30% 25%, #3a3a3a 0%, #222 45%, #141414 100%); }
  .about-badge { position: absolute; left: 403px; top: 40px; width: 20px; height: 20px; border-radius: 50%; background: var(--orange); }
  .about-title { position: absolute; left: 0; width: 825px; top: 72px; text-align: center; font-family: "Dosis", sans-serif; font-weight: 400; font-size: 24px; color: var(--white); }
  .about-lead { position: absolute; left: 160px; width: 505px; top: 106px; text-align: center; font-size: 10.5px; line-height: 12.8px; color: var(--white); }

  .role-card { position: absolute; width: 326px; height: 154px; background: var(--white); }
  .role-card h3 { position: absolute; left: 20px; top: 27px; font-size: 12.3px; font-weight: 700; color: #111; }
  .role-card .rule { position: absolute; left: 20px; top: 50px; width: 24px; height: 2.5px; background: var(--orange); }
  .role-card p { position: absolute; left: 20px; top: 63px; width: 165px; font-size: 8.4px; line-height: 9.8px; color: #222; }
  .role-card .btn { position: absolute; left: 20px; top: 106px; height: 16px; padding: 0 7px; background: var(--btn-dark); color: var(--white); font-size: 6.8px; line-height: 16px; }
  .role-card svg { position: absolute; left: 202px; top: 16px; }
  .card-a { left: 83px; top: 159px; }
  .card-b { left: 415px; top: 159px; }
  .card-c { left: 83px; top: 317px; }
  .card-d { left: 415px; top: 317px; }

  /* Footer */
  .site-footer { position: absolute; left: 0; top: 947px; width: 825px; height: 221px; background: var(--orange); }
  .footer-links { position: absolute; top: 59px; list-style: none; }
  .footer-links li { font-size: 9.2px; line-height: 15.5px; color: var(--white); }
  .footer-links li::before { content: "›"; margin-right: 4px; }
  .links-pages { left: 83px; }
  .links-social { left: 165px; }
  .field { position: absolute; border: 1px solid rgba(255,255,255,.9); color: var(--white); font-size: 8.5px; letter-spacing: .3px; padding: 9px 12px; }
  .field-user { left: 391px; top: 57px; width: 173px; height: 27px; }
  .field-email { left: 568px; top: 57px; width: 173px; height: 27px; }
  .field-comments { left: 391px; top: 90px; width: 350px; height: 53px; padding-top: 7px; }
  .send { position: absolute; left: 391px; top: 148px; width: 82px; height: 28px; border: 1px solid var(--white); color: var(--white); font-family: "Dosis", sans-serif; font-size: 12.5px; line-height: 26px; text-align: center; }

  .legal { position: absolute; left: 0; top: 1168px; width: 825px; height: 32px; background: var(--footer-bar); color: var(--white); font-size: 8.5px; line-height: 32px; padding-left: 85px; }
</style>
</head>
<body>

<header class="site-header">
  <div class="brand"><span class="brand-mark"></span><span class="brand-name">Veltra</span></div>
  <div class="follow">FOLLOW US ↓</div>
  <nav class="main-nav">
    <a href="#">ABOUT</a>
    <a href="#" class="is-active">SERVICES</a>
    <a href="#">PARTNER</a>
    <a href="#">CLIENTS</a>
    <a href="#">CONTACT</a>
  </nav>
</header>

<section class="hero">
  <div class="hero-photo" role="img" aria-label="Black and white photo of a city skyline with skyscrapers beside a river at dusk"></div>
  <div class="hero-panel">
    <h1 class="hero-title">YOU NEED INTEGRATION. WE'RE INVISIBLE &nbsp;BUT ALWAYS<br>SUPPORTING YOU.</h1>
    <p class="hero-text">Veltra is one of the leading systems integrators to the world's finance sector. We are an extension of your business and our services portfolio has been built so you always have access to a complete partner.</p>
  </div>
  <div class="hero-cta">LEARN MORE</div>
</section>

<section class="about">
  <div class="about-photo" role="img" aria-label="Dark, faded photo of business people in a meeting"></div>
  <span class="about-badge"></span>
  <h2 class="about-title">Who we are ?</h2>
  <p class="about-lead">If you're working a financial organisation, we have the servies to help everyone in your organisation work more efficiently, productively and profitably.</p>

  <article class="role-card card-a">
    <h3>Hedgefund Partner/CEO</h3><span class="rule"></span>
    <p>Lorem ipsum dolor sit amet, consectetur adipisicing elit, sed do eiusmod incididunt ut labore et dolore magna.</p>
    <span class="btn">LEARN MORE</span>
    <svg width="110" height="126" viewBox="0 0 110 126" role="img" aria-label="Photo of a businessman standing in a bright office">
      <defs><linearGradient id="g1" x1="0" y1="0" x2="1" y2="1"><stop offset="0" stop-color="#e4e8ec"/><stop offset="1" stop-color="#9fa9b3"/></linearGradient></defs>
      <polygon points="55,0 110,31.5 110,94.5 55,126 0,94.5 0,31.5" fill="url(#g1)"/>
    </svg>
  </article>

  <article class="role-card card-b">
    <h3>CFO</h3><span class="rule"></span>
    <p>Lorem ipsum dolor sit amet, consectetur adipisicing elit, sed do eiusmod incididunt ut labore et dolore magna.</p>
    <span class="btn">LEARN MORE</span>
    <svg width="110" height="126" viewBox="0 0 110 126" role="img" aria-label="Portrait photo of a senior executive in a suit">
      <defs><linearGradient id="g2" x1="0" y1="0" x2="0" y2="1"><stop offset="0" stop-color="#d8d2c6"/><stop offset="1" stop-color="#2f3b52"/></linearGradient></defs>
      <polygon points="55,0 110,31.5 110,94.5 55,126 0,94.5 0,31.5" fill="url(#g2)"/>
    </svg>
  </article>

  <article class="role-card card-c">
    <h3>CTO</h3><span class="rule"></span>
    <p>Lorem ipsum dolor sit amet, consectetur adipisicing elit, sed do eiusmod incididunt ut labore et dolore magna.</p>
    <span class="btn">LEARN MORE</span>
    <svg width="110" height="126" viewBox="0 0 110 126" role="img" aria-label="Portrait photo of a businesswoman holding glasses">
      <defs><linearGradient id="g3" x1="0" y1="0" x2="1" y2="1"><stop offset="0" stop-color="#2f8a8c"/><stop offset="1" stop-color="#e9e4df"/></linearGradient></defs>
      <polygon points="55,0 110,31.5 110,94.5 55,126 0,94.5 0,31.5" fill="url(#g3)"/>
    </svg>
  </article>

  <article class="role-card card-d">
    <h3>Employee</h3><span class="rule"></span>
    <p>Lorem ipsum dolor sit amet, consectetur adipisicing elit, sed do eiusmod incididunt ut labore et dolore magna.</p>
    <span class="btn">LEARN MORE</span>
    <svg width="110" height="126" viewBox="0 0 110 126" role="img" aria-label="Portrait photo of a businessman holding a folder">
      <defs><linearGradient id="g4" x1="0" y1="0" x2="0" y2="1"><stop offset="0" stop-color="#dfe3e6"/><stop offset="1" stop-color="#3a4250"/></linearGradient></defs>
      <polygon points="55,0 110,31.5 110,94.5 55,126 0,94.5 0,31.5" fill="url(#g4)"/>
    </svg>
  </article>
</section>

<footer class="site-footer">
  <ul class="footer-links links-pages">
    <li>Home</li><li>About</li><li>Services</li><li>Partners</li><li>Clients</li><li>Contacts</li>
  </ul>
  <ul class="footer-links links-social">
    <li>Friendwall</li><li>Chirpline</li><li>Circlecast</li><li>Workmesh</li>
  </ul>
  <div class="field field-user">User</div>
  <div class="field field-email">Email</div>
  <div class="field field-comments">Comments</div>
  <div class="send">Send</div>
</footer>

<div class="legal">© Copyright © 2015, Veltra Inc. All Rights Reserved</div>

</body>
</html>
```